New Zealand health product business needs website designed

A website is required for a business that sells New Zealand made products, namely products like infant formula, health products such as NZ honey, supplements, skincare products etc. This is purely an informative website that will introduce the all the different types of products the business has to offer. The target audience will the the Chinese market. The logo is a calligraphy style font in colours 78b643 and 313542 (logo is still being finalised at the moment) so a colour theme to match would be great.

It is crucial that the design communicates the beautiful nature of New Zealand, non-polluted environments, with emphasis on pure, natural and cleaniness.
Updates

A website that I quite like is http://www.frostvalegelato.co.nz

Information is easy to find, layout is nice and clear.                          

Hi all, I have now uploaded a logo for the business "Tawny Crate", please note that this is yet to be finalized however I expect it to be minor changes so please ensure the website theme and colour use go well with the logo. 

There are three scenery images uploaded, designs with any one of them used is fine whichever works better with your design.  Only one image is required on the website, no sliding effects for this.

Also just to clarify my requirements further.  The developer can use HTML, PHP, Javascript, CSS for coding, preferably to have the images cut and a pdf guide provided for things like alignment and sizing etc.

The menu items are Home / Our story / Product outline / Brands / Contact us
Designs are required for all these.  Within the product outline page, the subcategories are -
Infant formulas
Baby supplements
Toddlers products
Honey
Beauty products
Mens supplements
Womens supplements
Health products
Others

   

Target Market(s)

China based customers looking for quality products from New Zealand.

Industry/Entity Type

Health

Requirements
Must have
• clear menu bar in home page, the four main menu items are -
Our story
Product outline
Brands
Contact us
Nice to have
• Space for a large scenery photo in the home page

```html
<!DOCTYPE html>
<html lang="en">
<head>
<meta charset="utf-8">
<title>Tawny Crate – Health Products</title>
<link rel="stylesheet" href="https://fonts.googleapis.com/css2?family=Open+Sans:wght@400;600;700&display=swap">
<style>
  :root {
    --ink-dark: #2f323f;
    --ink-footer: #292b35;
    --card-bg: #30333f;
    --brand-green: #78b643;
    --text-light: #ffffff;
    --text-soft: #e6e7ea;
    --icon-bg: #1c1d22;
    --social-a: #8f95a8;
    --social-b: #a7acbb;
    --social-c: #bfc3cf;
  }
  * { margin: 0; padding: 0; box-sizing: border-box; }
  html, body { width: 1200px; height: 1000px; overflow: hidden; }
  body { font-family: "Open Sans", Arial, sans-serif; color: var(--text-light); background: var(--ink-dark); }
  .page { position: relative; width: 1200px; height: 1000px; overflow: hidden; }

  /* Header */
  .site-header { position: absolute; inset: 0 0 auto 0; height: 133px; background: var(--ink-dark); }
  .brand { position: absolute; left: 114px; top: 62px; display: flex; align-items: center; gap: 12px; }
  .brand-dot { width: 26px; height: 26px; border-radius: 50%; background: var(--text-light); }
  .brand-name { font-size: 36px; font-weight: 400; color: var(--text-light); letter-spacing: .5px; line-height: 1; }
  .call-us { position: absolute; left: 682px; top: 30px; font-size: 13px; color: var(--brand-green); font-family: Arial, sans-serif; }
  .utility { position: absolute; left: 893px; top: 18px; display: flex; align-items: center; font-size: 14px; font-family: Arial, sans-serif; }
  .utility .sep { margin: 0 10px; }
  .utility .sep.last { margin: 0 16px 0 10px; }
  .buy-icon { width: 34px; height: 34px; border-radius: 50%; background: var(--icon-bg); display: flex; align-items: center; justify-content: center; margin-right: 9px; }
  .main-nav { position: absolute; left: 545px; top: 88px; display: flex; font-size: 14px; font-family: Arial, sans-serif; letter-spacing: .3px; }
  .main-nav .sep { margin: 0 16px; }

  /* Hero scenery */
  .scenery { position: absolute; left: 0; top: 133px; width: 1200px; height: 794px;
    background:
      radial-gradient(ellipse 420px 300px at 1080px 330px, rgba(255,214,90,.95), rgba(240,160,50,.55) 40%, rgba(0,0,0,0) 75%),
      radial-gradient(ellipse 500px 160px at 560px 60px, rgba(240,190,110,.7), rgba(0,0,0,0) 70%),
      linear-gradient(180deg, #4a4a4c 0%, #8b7a63 18%, #c9a35e 34%, #7d735c 48%, #3f5a66 60%, #2f4b55 72%, #2d3a2a 86%, #1e2418 100%); }

  /* Section tab */
  .section-tab { position: absolute; left: 104px; top: 174px; width: 242px; height: 49px; background: var(--ink-dark); }
  .section-tab h1 { font-size: 18px; font-weight: 700; letter-spacing: .6px; padding: 13px 0 0 16px; word-spacing: 4px; }
  .section-tab::after { content: ""; position: absolute; left: 210px; top: 49px; border-left: 9px solid transparent; border-right: 9px solid transparent; border-top: 10px solid var(--ink-dark); }

  /* Product grid */
  .product-grid { position: absolute; left: 104px; top: 249px; display: grid; grid-template-columns: repeat(4, 245px); column-gap: 7px; row-gap: 22px; }
  .product-card { height: 309px; background: var(--card-bg); padding: 0 14px; position: relative; }
  .product-name { font-size: 17.5px; font-weight: 600; padding-top: 16px; height: 54px; letter-spacing: .2px; }
  .product-photo { width: 218px; height: 168px;
    background:
      radial-gradient(circle 62px at 150px 90px, #f3a21f, #e8861a 70%, #f6e9cf 72%, rgba(0,0,0,0) 78%),
      linear-gradient(135deg, #fff6dc 0%, #fde7b3 45%, #fbf3e6 100%); }
  .product-desc { font-size: 11.2px; line-height: 15.5px; color: var(--text-soft); text-align: justify; margin-top: 17px; hyphens: auto; }
  .read-more { position: absolute; right: 14px; bottom: 8px; font-size: 11.2px; color: var(--text-soft); }

  /* Footer */
  .site-footer { position: absolute; left: 0; top: 927px; width: 1200px; height: 73px; background: var(--ink-footer); }
  .copyright { position: absolute; left: 130px; top: 30px; font-size: 13px; font-family: Arial, sans-serif; }
  .follow { position: absolute; left: 898px; top: 22px; display: flex; align-items: center; gap: 7px; font-size: 12.5px; font-family: Arial, sans-serif; }
  .follow span { margin-right: 10px; }
  .social { width: 30px; height: 30px; border-radius: 50%; }
  .social.a { background: var(--social-a); }
  .social.b { background: var(--social-b); }
  .social.c { background: var(--social-c); }
</style>
</head>
<body>
<div class="page">
  <div class="scenery" role="img" aria-label="New Zealand coastal scenery at sunset: bay, beach, hills and golden sky"></div>

  <header class="site-header">
    <div class="brand"><span class="brand-dot"></span><span class="brand-name">Tawny Crate</span></div>
    <div class="call-us">CALL US AT : 000-123456789</div>
    <div class="utility">
      <span>Login</span><span class="sep">|</span><span>Help</span><span class="sep last">|</span>
      <span class="buy-icon">
        <svg width="18" height="16" viewBox="0 0 18 16" aria-hidden="true">
          <path d="M1 7 L9 1 L17 7" fill="none" stroke="#fff" stroke-width="2"/>
          <rect x="3.5" y="7" width="11" height="8" fill="#fff"/>
          <rect x="7.5" y="10" width="3" height="5" fill="#1c1d22"/>
        </svg>
      </span>
      <span>Buy</span>
    </div>
    <nav class="main-nav">
      <span>HOME</span><span class="sep">/</span>
      <span>OUR STORY</span><span class="sep">/</span>
      <span>PRODUCT ONLINE</span><span class="sep">/</span>
      <span>BRANDS</span><span class="sep">/</span>
      <span>CONTACT US</span>
    </nav>
  </header>

  <div class="section-tab"><h1>HEALTH PRODUCTS</h1></div>

  <main class="product-grid">
    <article class="product-card"><h2 class="product-name">PRODUCT NAME</h2><div class="product-photo" role="img" aria-label="Honey jar product photo"></div><p class="product-desc">Kauri Bloom Honey prides itself on sourcing honey products that enhance the well-being of our customers.</p><span class="read-more">read more...</span></article>
    <article class="product-card"><h2 class="product-name">PRODUCT NAME</h2><div class="product-photo" role="img" aria-label="Honey jar product photo"></div><p class="product-desc">Kauri Bloom Honey prides itself on sourcing honey products that enhance the well-being of our customers.</p><span class="read-more">read more...</span></article>
    <article class="product-card"><h2 class="product-name">PRODUCT NAME</h2><div class="product-photo" role="img" aria-label="Honey jar product photo"></div><p class="product-desc">Kauri Bloom Honey prides itself on sourcing honey products that enhance the well-being of our customers.</p><span class="read-more">read more...</span></article>
    <article class="product-card"><h2 class="product-name">PRODUCT NAME</h2><div class="product-photo" role="img" aria-label="Honey jar product photo"></div><p class="product-desc">Kauri Bloom Honey prides itself on sourcing honey products that enhance the well-being of our customers.</p><span class="read-more">read more...</span></article>
    <article class="product-card"><h2 class="product-name">PRODUCT NAME</h2><div class="product-photo" role="img" aria-label="Honey jar product photo"></div><p class="product-desc">Kauri Bloom Honey prides itself on sourcing honey products that enhance the well-being of our customers.</p><span class="read-more">read more...</span></article>
    <article class="product-card"><h2 class="product-name">PRODUCT NAME</h2><div class="product-photo" role="img" aria-label="Honey jar product photo"></div><p class="product-desc">Kauri Bloom Honey prides itself on sourcing honey products that enhance the well-being of our customers.</p><span class="read-more">read more...</span></article>
    <article class="product-card"><h2 class="product-name">PRODUCT NAME</h2><div class="product-photo" role="img" aria-label="Honey jar product photo"></div><p class="product-desc">Kauri Bloom Honey prides itself on sourcing honey products that enhance the well-being of our customers.</p><span class="read-more">read more...</span></article>
    <article class="product-card"><h2 class="product-name">PRODUCT NAME</h2><div class="product-photo" role="img" aria-label="Honey jar product photo"></div><p class="product-desc">Kauri Bloom Honey prides itself on sourcing honey products that enhance the well-being of our customers.</p><span class="read-more">read more...</span></article>
  </main>

  <footer class="site-footer">
    <p class="copyright">© 2013 Tawny Crate.com. All Rights Reserved.</p>
    <div class="follow">
      <span>FOLLOW US</span>
      <i class="social a" aria-label="Social link"></i>
      <i class="social b" aria-label="Social link"></i>
      <i class="social c" aria-label="Social link"></i>
    </div>
  </footer>
</div>
</body>
</html>
```